Doctors clinic requires stationary designed

We require various types of stationary to be design based on the logo (attached). We require the following:
- Letterhead (A4 Portrait)
- Business Card (must include UV spot on rear)
- With compliments slip (DL Landscape)
- Appointments card (Folded A6)

We are a young clinical practice which boasts a modern and sophisticated approach to medicine so we require something which feels fresh and modern. Please include colours represented in the logo (contrasting teal and grey). We are calling for creative minds to put forth their ideas and we will be actively providing feedback on all designs.

thank you

Clinic

```html
<!DOCTYPE html>
<html lang="en">
<head>
<meta charset="utf-8">
<title>Dr Laura Whitfield – Stationery Set</title>
<link href="https://fonts.googleapis.com/css2?family=Source+Sans+3:wght@400;600;700&family=Great+Vibes&display=swap" rel="stylesheet">
<style>
  :root{
    --teal:#1b998b;
    --teal-light:#d9ecea;
    --grey:#555a5c;
    --grey-soft:#8a8f91;
    --paper:#ffffff;
    --stage:#e9e7e4;
    --sans:"Source Sans 3", Arial, sans-serif;
    --script:"Great Vibes", cursive;
  }
  *{box-sizing:border-box;margin:0;padding:0}
  html,body{width:1200px;height:838px;overflow:hidden;background:var(--stage);font-family:var(--sans);color:var(--grey)}
  .canvas{position:relative;width:1200px;height:838px}
  .sheet{position:absolute;background:var(--paper);box-shadow:0 1px 4px rgba(0,0,0,.18);overflow:hidden}
  .band{position:absolute;left:0;right:0;bottom:0;background:var(--teal);color:#fff;text-align:center}
  .band::before{content:"";position:absolute;left:0;right:0;top:-4px;height:1px;background:var(--teal)}
  .brand{position:absolute;display:flex;align-items:center;gap:10px;color:var(--teal);font-weight:700;white-space:nowrap}
  .brand .dot{border:3px solid var(--teal);border-radius:50%;flex:none}
  .address{position:absolute;text-align:right;line-height:1.6}
  .contacts{position:absolute;line-height:1.6;border-left:1px solid #c9cccd}
  .contacts li{list-style:none;display:flex;align-items:center;gap:5px}
  .contacts svg{flex:none;fill:none;stroke:var(--teal);stroke-width:1.4}

  /* compliments slip */
  .slip{left:27px;top:194px;width:549px;height:258px}
  .slip .brand{left:158px;top:16px;font-size:25px}
  .slip .brand .dot{width:58px;height:58px}
  .slip .greeting{position:absolute;left:0;right:0;top:84px;text-align:center;font-family:var(--script);font-size:50px;color:var(--grey)}
  .slip .address{right:297px;top:186px;font-size:10px}
  .slip .contacts{left:262px;top:184px;padding-left:8px;font-size:10px}
  .slip .band{height:15px;font-size:11px;letter-spacing:3px;line-height:15px}

  /* business cards */
  .card-front{left:38px;top:481px;width:264px;height:150px}
  .card-front .brand{left:52px;top:18px;font-size:14px;gap:7px}
  .card-front .brand .dot{width:40px;height:40px;border-width:2px}
  .card-front .address{right:152px;top:82px;font-size:7px}
  .card-front .contacts{left:118px;top:81px;padding-left:4px;font-size:7px;line-height:1.5}
  .card-front .band{height:15px;font-size:9px;font-weight:700;line-height:15px}
  .card-front .band small{font-size:6px;font-weight:400}
  .card-back{left:318px;top:481px;width:264px;height:150px}
  .card-back .brand{left:48px;top:48px;font-size:14px;gap:7px}
  .card-back .brand .dot{width:40px;height:40px;border-width:2px}
  .card-back .site{position:absolute;left:0;right:0;top:116px;text-align:center;font-size:8px;letter-spacing:1.5px}
  .label{position:absolute;top:638px;font-size:8px;color:var(--grey)}

  /* letterhead */
  .letterhead{left:612px;top:34px;width:548px;height:775px}
  .letterhead .brand{left:20px;top:12px;font-size:19px}
  .letterhead .brand .dot{width:58px;height:58px}
  .letterhead .contacts{left:375px;top:12px;padding-left:10px;font-size:8px;line-height:1.5}
  .letterhead .contacts .addr{display:block;margin-top:3px}
  .letterhead .watermark{position:absolute;left:182px;top:289px;width:186px;height:198px;border:4px solid var(--teal-light);border-radius:50%}
  .letterhead .band{height:14px;font-size:10px;letter-spacing:3px;line-height:14px}
</style>
</head>
<body>
<main class="canvas">

  <section class="sheet slip" aria-label="With compliments slip">
    <div class="brand"><span class="dot"></span>Dr Laura Whitfield</div>
    <p class="greeting">With Compliments</p>
    <p class="address">Suite 4 Harbour Med.<br>Centre (West)Linden Ave<br>Brookvale, Zip Code - 000000</p>
    <ul class="contacts">
      <li><svg width="9" height="9" viewBox="0 0 10 10"><path d="M2 1l2 2-1 1.5a6 6 0 0 0 2.5 2.5L7 6l2 2-1.5 1.5C4 9 1 6 .5 2.5z"/></svg>9312 5580</li>
      <li><svg width="9" height="9" viewBox="0 0 10 10"><rect x="1" y="4" width="8" height="5"/><path d="M3 4V1h4v3"/></svg>9312 5580</li>
      <li><svg width="9" height="9" viewBox="0 0 10 10"><rect x="1" y="2.5" width="8" height="5.5"/><path d="M1 2.5l4 3 4-3"/></svg>your.names@drlaurawhitfield.com.au</li>
    </ul>
    <div class="band">www.drlaurawhitfield.com.au</div>
  </section>

  <section class="sheet card-front" aria-label="Business card front">
    <div class="brand"><span class="dot"></span>Dr Laura Whitfield</div>
    <p class="address">Suite 4 Harbour Med.<br>Centre (West)Linden Ave<br>Brookvale, Zip Code - 000000</p>
    <ul class="contacts">
      <li><svg width="6" height="6" viewBox="0 0 10 10"><path d="M2 1l2 2-1 1.5a6 6 0 0 0 2.5 2.5L7 6l2 2-1.5 1.5C4 9 1 6 .5 2.5z"/></svg>9312 5580</li>
      <li><svg width="6" height="6" viewBox="0 0 10 10"><rect x="1" y="4" width="8" height="5"/><path d="M3 4V1h4v3"/></svg>9312 5580</li>
      <li><svg width="6" height="6" viewBox="0 0 10 10"><rect x="1" y="2.5" width="8" height="5.5"/><path d="M1 2.5l4 3 4-3"/></svg>your.names@drlaurawhitfield.com.au</li>
      <li><svg width="6" height="6" viewBox="0 0 10 10"><circle cx="5" cy="5" r="4"/><path d="M1 5h8M5 1v8"/></svg>www.drlaurawhitfield.com.au</li>
    </ul>
    <div class="band">Your Name, <small>Title</small></div>
  </section>
  <span class="label" style="left:140px">BC_FRONT</span>

  <section class="sheet card-back" aria-label="Business card back">
    <div class="brand"><span class="dot"></span>Dr Laura Whitfield</div>
    <p class="site">www.drlaurawhitfield.com</p>
  </section>
  <span class="label" style="left:431px">BC_BACK</span>

  <section class="sheet letterhead" aria-label="Letterhead">
    <div class="brand"><span class="dot"></span>Dr Laura Whitfield</div>
    <ul class="contacts">
      <li><svg width="7" height="7" viewBox="0 0 10 10"><path d="M2 1l2 2-1 1.5a6 6 0 0 0 2.5 2.5L7 6l2 2-1.5 1.5C4 9 1 6 .5 2.5z"/></svg>9312 5580</li>
      <li><svg width="7" height="7" viewBox="0 0 10 10"><rect x="1" y="4" width="8" height="5"/><path d="M3 4V1h4v3"/></svg>9312 5580</li>
      <li><svg width="7" height="7" viewBox="0 0 10 10"><rect x="1" y="2.5" width="8" height="5.5"/><path d="M1 2.5l4 3 4-3"/></svg>your.names@drlaurawhitfield.com.au</li>
      <li class="addr">Suite 4 Harbour Med. Centre (West)Linden Ave<br>Brookvale, Zip Code - 000000</li>
    </ul>
    <div class="watermark"></div>
    <div class="band">www.drlaurawhitfield.com.au</div>
  </section>

</main>
</body>
</html>
```